Fabric Softener

We need fabric softener. Bottle picture attached for reference. Color of bottle can be proposed as well. Normally bottle is pink and blue color

Logo is also attached that shall be used.
Updates

Need extra days to review

Low designer entries

Target Market(s)

Niche

Font styles to use
Sans Serif

Requirements
Must have
• Fabric, Brightness, Nature
Nice to have
• Good colors
Should not have
• Adults

```html
<!DOCTYPE html>
<html lang="en">
<head>
<meta charset="utf-8">
<title>Lumora Fabric Softener – Cherry Flowers Label</title>
<link rel="stylesheet" href="https://fonts.googleapis.com/css2?family=Amatic+SC:wght@700&family=Open+Sans:wght@400;600&display=swap">
<style>
  :root {
    --canvas: #ffffff;
    --sky: #a9cdec;
    --sky-light: #c4dcf2;
    --blossom: #f5c3d2;
    --blossom-light: #fbe1e9;
    --purple-deep: #6a45a0;
    --purple-band: #7d55ab;
    --purple-soft: #b49bd3;
    --title-blue: #1f4a9c;
    --title-shadow: #f3b3cb;
    --white: #ffffff;
    --bottle: #d6b0e4;
    --badge-blue: #2a73bd;
  }
  html, body {
    margin: 0;
    padding: 0;
    width: 1200px;
    height: 917px;
    overflow: hidden;
    background: var(--canvas);
  }
  .board { display: block; width: 1200px; height: 917px; }
  .sans { font-family: "Open Sans", Arial, sans-serif; }
  .display { font-family: "Amatic SC", "Arial Narrow", sans-serif; font-weight: 700; }
  .brand-name { font-family: "Open Sans", Arial, sans-serif; font-weight: 600; font-size: 50px; fill: var(--purple-deep); }
  .freshness-text { font-size: 12.5px; fill: var(--white); }
  .title { font-size: 86px; fill: var(--title-blue); }
  .title-shadow { font-size: 86px; fill: var(--title-shadow); }
  .scent { font-size: 42px; fill: var(--white); }
  .loads-number { font-size: 22px; fill: var(--title-blue); }
  .loads-label { font-size: 13px; fill: var(--purple-deep); }
  .product-type { font-size: 15.5px; fill: var(--white); }
  .volume { font-size: 22.5px; fill: var(--white); }
  .swatch-note { font-size: 31px; fill: var(--bottle); }
</style>
</head>
<body>
<svg class="board" viewBox="0 0 1200 917" xmlns="http://www.w3.org/2000/svg">
  <defs>
    <clipPath id="label-shape">
      <path d="M209,123 C150,125 118,260 100,380 C92,460 90,560 98,660 C104,760 130,794 200,794 L420,793 C520,790 600,760 613,690 C620,640 620,580 612,540 C604,505 580,498 540,497 L478,496 C400,494 360,440 330,330 C310,240 280,123 209,123 Z"/>
    </clipPath>
    <linearGradient id="sky-fill" x1="0" y1="0" x2="0" y2="1">
      <stop offset="0" stop-color="var(--sky-light)"/>
      <stop offset="1" stop-color="var(--sky)"/>
    </linearGradient>
    <linearGradient id="blossom-fill" gradientUnits="userSpaceOnUse" x1="180" y1="130" x2="300" y2="540">
      <stop offset="0" stop-color="var(--blossom)" stop-opacity="1"/>
      <stop offset="0.6" stop-color="var(--blossom)" stop-opacity="0.9"/>
      <stop offset="1" stop-color="var(--blossom)" stop-opacity="0"/>
    </linearGradient>
    <linearGradient id="lower-band" x1="0" y1="0" x2="1" y2="0">
      <stop offset="0" stop-color="var(--purple-soft)"/>
      <stop offset="0.55" stop-color="var(--purple-band)"/>
      <stop offset="1" stop-color="var(--purple-deep)"/>
    </linearGradient>
    <radialGradient id="flower-fill" cx="0.5" cy="0.5" r="0.5">
      <stop offset="0" stop-color="var(--blossom-light)"/>
      <stop offset="0.7" stop-color="var(--blossom)"/>
      <stop offset="1" stop-color="var(--blossom)" stop-opacity="0"/>
    </radialGradient>
  </defs>

  <g class="label" clip-path="url(#label-shape)">
    <rect class="label-background" x="90" y="120" width="530" height="680" fill="url(#sky-fill)"/>
    <rect class="blossom-branch-art" x="90" y="120" width="530" height="430" fill="url(#blossom-fill)" role="img" aria-label="Illustration of pink cherry blossoms on branches"/>
    <path class="scent-band" d="M90,648 C220,636 420,632 620,648 L620,712 C420,702 220,704 90,714 Z" fill="var(--purple-band)"/>
    <rect class="base-band" x="90" y="708" width="530" height="92" fill="url(#lower-band)"/>
    <circle class="flower-art" cx="176" cy="715" r="78" fill="url(#flower-fill)" role="img" aria-label="Illustration of a single pink cherry flower"/>
  </g>

  <g class="freshness-badge">
    <circle cx="216" cy="203" r="40" fill="var(--purple-deep)"/>
    <text class="sans freshness-text" x="216" y="193" text-anchor="middle">30 days</text>
    <text class="sans freshness-text" x="216" y="207" text-anchor="middle">of</text>
    <text class="sans freshness-text" x="216" y="221" text-anchor="middle">freshness</text>
  </g>

  <text class="brand-name" x="218" y="384" text-anchor="middle">Lumora</text>

  <g class="product-title display">
    <text class="title-shadow" x="218" y="558" textLength="213" lengthAdjust="spacingAndGlyphs">FABRIC</text>
    <text class="title" x="214" y="555" textLength="213" lengthAdjust="spacingAndGlyphs">FABRIC</text>
    <text class="title-shadow" x="168" y="625" textLength="317" lengthAdjust="spacingAndGlyphs">SOFTENER</text>
    <text class="title" x="164" y="622" textLength="317" lengthAdjust="spacingAndGlyphs">SOFTENER</text>
  </g>

  <circle class="washer-badge" cx="553" cy="575" r="26" fill="var(--badge-blue)"/>

  <text class="display scent" x="255" y="688" textLength="180" lengthAdjust="spacingAndGlyphs">Cherry Flowers</text>

  <g class="loads-badge">
    <circle cx="511" cy="664" r="34" fill="var(--white)"/>
    <text class="sans loads-number" x="511" y="660" text-anchor="middle">50</text>
    <text class="sans loads-label" x="511" y="676" text-anchor="middle">small</text>
    <text class="sans loads-label" x="511" y="690" text-anchor="middle">loads</text>
  </g>

  <text class="sans product-type" x="350" y="747" text-anchor="middle">fabric conditioner</text>
  <text class="sans volume" x="350" y="775" text-anchor="middle">2 Liters/67.63 oz</text>

  <g class="bottle-colour-note">
    <circle cx="650" cy="164" r="32" fill="var(--bottle)"/>
    <text class="sans swatch-note" x="704" y="36">bottle collor</text>
    <text class="sans swatch-note" x="704" y="76">#d6b0e4</text>
  </g>
</svg>
</body>
</html>
```